Business Card Design

We need a business card for our established Fruit and Veg shop that offers retail and wholesale to the public. We offer a range of Australian products and also provide nuts, confectionary, pasta's etc. We would like to use colours green, red, orange and yellow. The final design would use our photo of the shop and some produce and should communicate freshness and quality.

Target Market(s)

families, businesses

Industry/Entity Type

Retail

Contact Information for Business Card

Creekbend Produce Shed
Retail and Wholesale Fruit and Veg
Peter and Marco Bellucci - Manager
47 Carrow Valley Road, Penwick Flat S.A. 5172
Ph: (08) 8294 5613
Fax: (08) 8294 5713
creekbendproduceshed@mailbrook.net
www.friendspage.net/CreekbendProduceShed
Open 7 Days

Requirements
Must have
• The photo of the shop
Nice to have
• Both the photos

```html
<!DOCTYPE html>
<html lang="en">
<head>
<meta charset="utf-8">
<title>Creekbend Produce Shed – Business Card</title>
<link href="https://fonts.googleapis.com/css2?family=Tinos&family=Arimo:wght@400;700&display=swap" rel="stylesheet">
<style>
  :root {
    --red: #e32226;
    --red-dark: #d81e22;
    --yellow: #fff200;
    --sun: #fed300;
    --green: #9dbb3b;
    --ink: #555555;
    --white: #ffffff;
    --page: #ecebe7;
  }
  * { margin: 0; padding: 0; box-sizing: border-box; }
  html, body { width: 1200px; height: 1000px; overflow: hidden; background: var(--page); }
  .card {
    position: absolute; left: 220px; width: 760px; height: 440px;
    border-radius: 34px; overflow: hidden; background: var(--white);
    box-shadow: 0 4px 14px rgba(0,0,0,.18);
  }
  .card--front { top: 40px; }
  .card--back { top: 520px; }
  .card svg.card__art { position: absolute; inset: 0; }

  /* front */
  .front__brand { position: absolute; left: 250px; top: 300px; width: 470px; text-align: center; color: var(--white); font-family: "Tinos", serif; }
  .brand__name { font-size: 34px; letter-spacing: 1px; display: inline-flex; align-items: center; gap: 12px; }
  .brand__dot { width: 22px; height: 22px; border-radius: 50%; background: var(--sun); display: inline-block; }
  .brand__tagline { font-size: 17px; letter-spacing: .5px; margin-top: 2px; }
  .front__hours { font-family: "Arimo", sans-serif; font-size: 26px; color: var(--sun); margin-top: 8px; }

  /* back */
  .back__brand {
    position: absolute; left: 198px; top: 220px; width: 400px;
    transform: translate(-50%, -50%) rotate(-90deg);
    text-align: center; color: var(--white); font-family: "Tinos", serif;
  }
  .back__brand .brand__name { font-size: 28px; }
  .back__brand .brand__tagline { font-size: 14px; }

  .back__details { position: absolute; left: 418px; top: 58px; width: 320px; font-family: "Arimo", sans-serif; color: var(--ink); }
  .person__name { color: var(--red); font-weight: 700; font-size: 23px; }
  .person__role { font-size: 22px; margin-top: 2px; }
  .rule { height: 2px; background: var(--sun); margin: 16px 0 18px; }
  .contact { list-style: none; font-size: 14.5px; line-height: 23px; }
  .contact li { display: flex; align-items: center; gap: 10px; }
  .contact svg { flex: none; }
  .address { font-size: 18px; line-height: 25px; }
</style>
</head>
<body>

<section class="card card--front">
  <svg class="card__art" width="760" height="440" viewBox="0 0 760 440">
    <defs>
      <linearGradient id="shopTone" x1="0" y1="0" x2="0" y2="1">
        <stop offset="0" stop-color="#dfe5ea"/>
        <stop offset=".45" stop-color="#6f7a80"/>
        <stop offset="1" stop-color="#b9b6ae"/>
      </linearGradient>
      <linearGradient id="produceTone" x1="0" y1="0" x2="1" y2="1">
        <stop offset="0" stop-color="#e0593c"/>
        <stop offset=".5" stop-color="#e8c25a"/>
        <stop offset="1" stop-color="#9a9a8c"/>
      </linearGradient>
    </defs>
    <rect class="photo photo--shop" role="img" aria-label="Photo of the shop front with produce stands under the awning" x="0" y="0" width="500" height="330" fill="url(#shopTone)"/>
    <path class="photo photo--produce" role="img" aria-label="Photo of fresh apples and bananas on display inside the shop" d="M420 0 H760 V330 H470 Q520 170 420 0 Z" fill="url(#produceTone)"/>
    <path d="M0 318 Q400 250 760 170 V440 H0 Z" fill="var(--green)"/>
    <path d="M0 326 Q400 258 760 178 V440 H0 Z" fill="var(--yellow)"/>
    <path d="M0 334 Q400 266 760 186 V440 H0 Z" fill="var(--red)"/>
  </svg>
  <div class="front__brand">
    <div class="brand__name"><span class="brand__dot"></span>CREEKBEND PRODUCE SHED</div>
    <div class="brand__tagline">RETAIL AND WHOLESALE FRUIT AND VEG</div>
    <div class="front__hours">Open 7 Days</div>
  </div>
</section>

<section class="card card--back">
  <svg class="card__art" width="760" height="440" viewBox="0 0 760 440">
    <rect x="0" y="0" width="70" height="440" fill="var(--green)"/>
    <path d="M70 0 H372 Q360 240 408 440 H70 Z" fill="var(--green)"/>
    <path d="M70 0 H364 Q352 240 400 440 H70 Z" fill="var(--yellow)"/>
    <path d="M70 0 H356 Q344 240 392 440 H70 Z" fill="var(--red)"/>
  </svg>
  <div class="back__brand">
    <div class="brand__name">CREEKBEND PRODUCE SHED</div>
    <div class="brand__tagline">RETAIL AND WHOLESALE FRUIT AND VEG</div>
  </div>

  <div class="back__details">
    <div class="person__name">Peter and Marco Bellucci</div>
    <div class="person__role">Manager</div>
    <div class="rule"></div>
    <ul class="contact">
      <li>
        <svg width="18" height="18" viewBox="0 0 18 18"><circle cx="9" cy="9" r="9" fill="var(--green)"/><rect x="6" y="4" width="6" height="10" rx="1.2" fill="none" stroke="#fff" stroke-width="1.4"/></svg>
        (08) 8294 5613
      </li>
      <li>
        <svg width="18" height="18" viewBox="0 0 18 18"><circle cx="9" cy="9" r="9" fill="var(--green)"/><rect x="5" y="7" width="8" height="6" fill="none" stroke="#fff" stroke-width="1.4"/><rect x="6.5" y="4" width="5" height="3" fill="#fff"/></svg>
        (08) 8294 5713
      </li>
      <li>
        <svg width="18" height="18" viewBox="0 0 18 18"><circle cx="9" cy="9" r="9" fill="var(--green)"/><rect x="4.5" y="6" width="9" height="6.5" fill="none" stroke="#fff" stroke-width="1.3"/><path d="M4.5 6 L9 10 L13.5 6" fill="none" stroke="#fff" stroke-width="1.3"/></svg>
        creekbendproduceshed@mailbrook.net
      </li>
      <li>
        <svg width="18" height="18" viewBox="0 0 18 18"><circle cx="9" cy="9" r="9" fill="var(--green)"/></svg>
        www.friendspage.net/CreekbendProduceShed
      </li>
    </ul>
    <div class="rule"></div>
    <div class="address">47 Carrow Valley Road,<br>Penwick Flat S.A. 5172</div>
  </div>
</section>

</body>
</html>
```